Brightwell Systems - Company Overview Brochure

We would like a single page A4 Brochure to give to new potential customers to provide a quick overview of our company. This will be used in presales meetings.

We have included the content we would like on the brochure under "Brightwell Systems Marketing Brochure.docx".

We have included two other designs "timebundleterms v4.pdf and Brightwell Public Cloud Plans.pdf" which shows similar marketing brochures we have. We would like these designs to have the same Brightwell Blue and "Specialised Technology Consultancy firm" theme.

Target Market(s)

Technology Sector

Industry/Entity Type

Information Technology

Colors
0054AA
0677BA
7BADD7
CADEEF
E8F1F8

Requirements
Must have
• "Innovative Tech Company Theme".

```html
<!DOCTYPE html>
<html lang="en">
<head>
<meta charset="utf-8">
<title>Brightwell Systems – Company Overview</title>
<link href="https://fonts.googleapis.com/css2?family=Oswald:wght@600;700&family=Inter:wght@400;500;600;700&display=swap" rel="stylesheet">
<style>
  :root{
    --navy:#0a2a6e;
    --deep:#06205a;
    --blue:#0054AA;
    --blue-mid:#0677BA;
    --blue-soft:#7BADD7;
    --blue-pale:#CADEEF;
    --mist:#E8F1F8;
    --ink:#1b2233;
    --body:#2a3142;
    --line:#c6d6e8;
    --white:#ffffff;
  }
  *{box-sizing:border-box;margin:0;padding:0}
  html,body{width:848px;height:1200px;overflow:hidden;background:var(--white)}
  body{font-family:"Inter",Arial,sans-serif;color:var(--body)}
  .page{position:relative;width:848px;height:1200px;overflow:hidden;
    background:linear-gradient(180deg,#f4f8fc 0%,#eef4fa 60%,#f3f7fb 100%)}
  .abs{position:absolute}

  /* hero */
  .hero-art{position:absolute;left:0;top:0;width:848px;height:504px}
  .hero-visual{left:0;top:0;width:848px;height:504px;
    clip-path:polygon(572px 0,848px 0,848px 504px,572px 504px,424px 265px);
    background:linear-gradient(180deg,#0d3d9e 0%,#0a2f7c 50%,#061a48 100%)}
  .brand{left:40px;top:38px;display:flex;align-items:center;gap:12px}
  .brand-mark{width:34px;height:34px;background:var(--blue);border-radius:4px}
  .brand-name{font-weight:700;font-size:27px;line-height:1.05;color:var(--blue);letter-spacing:.5px}
  .tagline{left:36px;top:130px;display:flex;align-items:center;gap:8px;font-size:13px;color:var(--blue);font-weight:500;white-space:nowrap}
  .tagline::before,.tagline::after{content:"";width:40px;height:1.5px;background:var(--blue)}
  .headline{left:40px;top:168px;font-family:"Oswald",sans-serif;font-weight:700;font-size:38px;line-height:1.24;letter-spacing:-.2px;color:var(--ink);text-transform:uppercase;white-space:nowrap}
  .headline .accent{color:var(--blue)}
  .intro{left:40px;top:282px;width:352px;font-size:12.8px;line-height:1.62;color:var(--body)}
  .hero-rule{left:40px;top:388px;width:412px;height:1px;background:var(--line)}
  .values{left:38px;top:407px;display:flex;align-items:center}
  .value{display:flex;align-items:center;gap:9px;font-size:11.2px;font-weight:600;color:var(--ink);line-height:1.35;padding:0 16px;white-space:nowrap}
  .value:first-child{padding-left:0}
  .value+.value{border-left:1px solid var(--line)}
  .value svg{width:34px;height:34px;flex:none}

  /* section tabs */
  .tab{height:30px;display:flex;align-items:center;padding:0 0 0 24px;color:var(--white);font-weight:700;font-size:14px;white-space:nowrap;letter-spacing:-.1px;
    background:var(--blue);clip-path:polygon(18px 0,100% 0,calc(100% - 18px) 100%,0 100%)}
  .tab-line{height:1px;background:var(--blue-soft)}

  /* services */
  .services{left:24px;top:538px;width:800px;display:grid;grid-template-columns:repeat(5,1fr)}
  .service{padding:0 10px 0 12px;border-left:1px solid var(--line);min-height:196px}
  .service:first-child{border-left:none;padding-left:16px}
  .service svg{display:block;width:72px;height:60px;margin:0 auto 18px}
  .service h3{font-size:11px;font-weight:700;color:var(--blue);text-transform:uppercase;letter-spacing:-.2px;margin-bottom:13px;line-height:1.35;white-space:nowrap}
  .service:last-child h3{text-align:center}
  .service p{font-size:11.2px;line-height:1.45;color:var(--body)}

  /* why */
  .why-list{left:44px;top:795px;width:316px}
  .why-item{display:flex;gap:14px;padding:6px 0;border-bottom:1px solid var(--line);height:59px}
  .why-item:last-child{border-bottom:none}
  .why-icon{width:40px;height:40px;border-radius:50%;background:var(--blue);flex:none;display:flex;align-items:center;justify-content:center}
  .why-icon svg{width:22px;height:22px}
  .why-item h4{font-size:11.4px;font-weight:700;color:var(--blue);margin-bottom:3px}
  .why-item p{font-size:11px;line-height:1.45;color:var(--body)}

  /* partners */
  .col-rule{left:388px;top:800px;width:1px;height:212px;background:var(--line)}
  .partners{left:408px;top:800px;width:408px;display:grid;grid-template-columns:1fr 1fr 1fr}
  .partner{text-align:center;padding:8px 0;height:70px;display:flex;flex-direction:column;justify-content:center;gap:4px}
  .partner+.partner{border-left:1px solid var(--line)}
  .partner-name{font-size:14px;font-weight:700;color:var(--ink);white-space:nowrap}
  .partner-note{font-size:10px;color:#4a5366}

  .quality{left:410px;top:899px;width:406px;height:130px;border:1px solid var(--blue-soft);border-radius:8px;background:var(--mist);overflow:hidden}
  .quality-flag{position:absolute;left:0;top:0;width:54px;height:82px;background:var(--blue);clip-path:polygon(0 0,100% 0,100% 80%,0 100%)}
  .quality-flag svg{position:absolute;left:13px;top:20px;width:28px;height:32px}
  .quality h4{position:absolute;left:65px;top:28px;font-size:10.4px;font-weight:700;color:var(--blue);letter-spacing:-.2px;white-space:nowrap}
  .quality p{position:absolute;left:65px;top:60px;width:200px;font-size:10px;line-height:1.65;color:var(--body)}
  .quality-divider{position:absolute;left:272px;top:12px;width:1px;height:106px;background:var(--line)}
  .cert{position:absolute;left:288px;display:flex;align-items:center;gap:10px}
  .cert-seal{width:34px;height:34px;border-radius:50%;border:2px solid var(--blue);background:var(--white);flex:none}
  .cert-text small{display:block;font-size:8px;font-weight:700;color:var(--navy)}
  .cert-text b{display:block;font-size:14px;font-weight:700;color:var(--navy);line-height:1.1}
  .cert-text span{display:block;font-size:6.4px;color:var(--ink);line-height:1.2}

  /* footer */
  .cta-band{left:0;top:1042px;width:848px;height:109px;background:linear-gradient(90deg,#082a6c 0%,#0b3380 50%,#082a6c 100%)}
  .cta{position:absolute;left:88px;top:28px;width:226px;color:var(--white)}
  .cta h5{font-size:12px;font-weight:700;margin-bottom:8px}
  .cta p{font-size:8.8px;line-height:1.7;color:#dbe6f5}
  .contact{position:absolute;top:26px;height:56px;display:flex;align-items:center;gap:10px;color:var(--white);padding-left:18px;border-left:1px solid rgba(255,255,255,.35)}
  .contact-dot{width:37px;height:37px;border-radius:50%;background:var(--blue-mid);display:flex;align-items:center;justify-content:center;flex:none}
  .contact-dot svg{width:19px;height:19px}
  .contact b{display:block;font-size:9.5px;font-weight:700;margin-bottom:6px}
  .contact span{display:block;font-size:8.2px;color:#e3ecf8;white-space:nowrap}
  .signoff{left:0;top:1151px;width:848px;height:49px;display:flex;align-items:center;justify-content:center;gap:18px;background:var(--mist);font-size:12.5px;color:var(--blue-mid)}
  .signoff b{font-weight:600;letter-spacing:.4px}
  .signoff i{width:1px;height:16px;background:var(--blue-soft)}
  .signoff span{letter-spacing:2.6px;font-size:11px}
</style>
</head>
<body>
<div class="page">

  <svg class="hero-art" viewBox="0 0 848 504" aria-hidden="true">
    <polygon points="515,0 848,0 848,504 548,504 398,265" fill="var(--blue-pale)"/>
    <polygon points="563,0 848,0 848,504 563,504 414,265" fill="var(--blue)"/>
  </svg>
  <div class="abs hero-visual" role="img" aria-label="Night city skyline with a glowing cloud and network lines rising above the buildings"></div>

  <div class="abs brand">
    <div class="brand-mark"></div>
    <div class="brand-name">BRIGHTWELL<br>SYSTEMS</div>
  </div>
  <div class="abs tagline">Specialised Technology Consultancy Firm</div>

  <h1 class="abs headline">Innovative Solutions.<br><span class="accent">Measurable Impact.</span></h1>

  <p class="abs intro">Brightwell Systems is a specialised technology consultancy firm delivering innovative, cloud-first and tailored solutions that help businesses modernise, optimise and grow in a rapidly evolving digital world.</p>

  <div class="abs hero-rule"></div>
  <div class="abs values">
    <div class="value">
      <svg viewBox="0 0 34 34" fill="none" stroke="var(--blue)" stroke-width="1.6"><circle cx="12" cy="10" r="4.5"/><circle cx="23" cy="10" r="4.5"/><path d="M3 30v-5a7 7 0 0 1 7-7h4M31 30v-5a7 7 0 0 0-7-7h-4"/><circle cx="17" cy="17" r="4.5"/><path d="M9 31v-3a6 6 0 0 1 6-6h4a6 6 0 0 1 6 6v3z"/></svg>
      <span>Client Focused</span>
    </div>
    <div class="value">
      <svg viewBox="0 0 34 34" fill="none" stroke="var(--blue)" stroke-width="1.6"><path d="M17 3a10 10 0 0 0-6 18c1.3 1 2 2.3 2 4h8c0-1.7.7-3 2-4A10 10 0 0 0 17 3z"/><path d="M13 28h8M14 31h6M17 25v-8l-3-3M17 17l3-3"/></svg>
      <span>Innovative<br>Solutions</span>
    </div>
    <div class="value">
      <svg viewBox="0 0 34 34" fill="none" stroke="var(--blue)" stroke-width="1.6"><path d="M17 3l11 4v9c0 7-5 12-11 15C11 28 6 23 6 16V7z"/><path d="M12 17l4 4 7-8"/></svg>
      <span>Trusted<br>Partnerships</span>
    </div>
  </div>

  <!-- services -->
  <div class="abs tab" style="left:24px;top:489px;width:162px">OUR SERVICES</div>
  <div class="abs tab-line" style="left:180px;top:503px;width:644px"></div>

  <div class="abs services">
    <div class="service">
      <svg viewBox="0 0 72 60" fill="none" stroke="var(--blue)" stroke-width="2"><path d="M18 46h38a10 10 0 0 0 0-20 14 14 0 0 0-26-6 11 11 0 0 0-12 26z"/></svg>
      <h3>Cloud Solutions</h3>
      <p>Secure, scalable and cost-efficient cloud implementations on Nimbus Cloud and Corvid Cloud.</p>
    </div>
    <div class="service">
      <svg viewBox="0 0 72 60" fill="none" stroke="var(--blue)" stroke-width="2"><path d="M30 6h8l1 6 5 2 5-4 6 6-4 5 2 5 6 1v8l-6 1-2 5 4 5-6 6-5-4-5 2-1 6h-8l-1-6-5-2-5 4-6-6 4-5-2-5-6-1v-8l6-1 2-5-4-5 6-6 5 4 5-2z"/><circle cx="34" cy="30" r="8"/><path d="M42 30h20M40 22l12-6M40 38l12 6"/><circle cx="63" cy="30" r="2"/><circle cx="54" cy="15" r="2"/><circle cx="54" cy="45" r="2"/></svg>
      <h3>DevOps &amp; Automation</h3>
      <p>Streamline delivery pipelines and infrastructure with DevOps best practices and automation.</p>
    </div>
    <div class="service">
      <svg viewBox="0 0 72 60" fill="none" stroke="var(--blue)" stroke-width="2"><path d="M36 2l22 8v18c0 14-10 24-22 30C24 52 14 42 14 28V10z"/><rect x="28" y="27" width="16" height="13" rx="1.5"/><path d="M31 27v-5a5 5 0 0 1 10 0v5"/><circle cx="36" cy="33" r="1.5"/></svg>
      <h3>Cyber Security</h3>
      <p>Protect your business with robust security frameworks, assessments and managed services.</p>
    </div>
    <div class="service">
      <svg viewBox="0 0 72 60" fill="none" stroke="var(--blue)" stroke-width="2"><rect x="6" y="40" width="8" height="16"/><rect x="22" y="32" width="8" height="24"/><rect x="38" y="36" width="8" height="20"/><rect x="54" y="26" width="8" height="30"/><path d="M8 26l14-12 14 8 14-10 12-6"/><circle cx="8" cy="26" r="2.5"/><circle cx="22" cy="14" r="2.5"/><circle cx="36" cy="22" r="2.5"/><circle cx="50" cy="12" r="2.5"/><circle cx="63" cy="6" r="2.5"/></svg>
      <h3>Data &amp; Analytics</h3>
      <p>Turn data into insights with modern data platforms, analytics and visualisation.</p>
    </div>
    <div class="service">
      <svg viewBox="0 0 72 60" fill="none" stroke="var(--blue)" stroke-width="2"><rect x="6" y="4" width="60" height="42" rx="2"/><path d="M6 38h60M30 46l-3 8h18l-3-8M22 54h28"/><path d="M28 16l-6 6 6 6M44 16l6 6-6 6M39 14l-6 16"/></svg>
      <h3>Software<br>Development</h3>
      <p>Custom application development that solves complex business challenges and drives innovation.</p>
    </div>
  </div>

  <!-- why -->
  <div class="abs tab" style="left:28px;top:758px;width:264px">WHY CHOOSE BRIGHTWELL?</div>
  <div class="abs tab-line" style="left:286px;top:772px;width:94px"></div>

  <div class="abs why-list">
    <div class="why-item">
      <div class="why-icon"><svg viewBox="0 0 22 22" fill="none" stroke="#fff" stroke-width="1.5"><circle cx="7" cy="7" r="3"/><circle cx="15" cy="7" r="3"/><path d="M2 19v-3a4 4 0 0 1 4-4h10a4 4 0 0 1 4 4v3z"/></svg></div>
      <div><h4>SPECIALISED EXPERTISE</h4><p>Deep technical knowledge across cloud, DevOps, security and modern engineering.</p></div>
    </div>
    <div class="why-item">
      <div class="why-icon"><svg viewBox="0 0 22 22" fill="none" stroke="#fff" stroke-width="1.5"><circle cx="11" cy="11" r="8.5"/><circle cx="11" cy="11" r="5"/><circle cx="11" cy="11" r="1.5"/><path d="M11 11l8-8M16 3h3v3"/></svg></div>
      <div><h4>TAILORED SOLUTIONS</h4><p>We design and deliver solutions aligned to your unique business goals.</p></div>
    </div>
    <div class="why-item">
      <div class="why-icon"><svg viewBox="0 0 22 22" fill="none" stroke="#fff" stroke-width="1.5"><path d="M19 3c-6 0-10 4-12 9l3 3c5-2 9-6 9-12z"/><circle cx="14" cy="8" r="1.5"/><path d="M7 12l-4 1 2-4h3M10 15l-1 4 4-2v-3M6 16l-3 3"/></svg></div>
      <div><h4>INNOVATION DRIVEN</h4><p>We leverage the latest technologies to deliver future-ready outcomes.</p></div>
    </div>
    <div class="why-item">
      <div class="why-icon"><svg viewBox="0 0 22 22" fill="none" stroke="#fff" stroke-width="1.5"><path d="M1 9l4-3 4 1 3-2 4 1 5 3M3 11l5 5c1 1 2 1 3 0l5-5M9 7l-3 3c1 1 2 1 3 0l2-1 4 4"/></svg></div>
      <div><h4>TRUE PARTNERSHIP</h4><p>Collaborative approach focused on long-term success and measurable value.</p></div>
    </div>
  </div>

  <div class="abs col-rule"></div>

  <!-- partners -->
  <div class="abs tab" style="left:406px;top:759px;width:282px">OUR TECHNOLOGY PARTNERS</div>
  <div class="abs tab-line" style="left:682px;top:773px;width:134px"></div>

  <div class="abs partners">
    <div class="partner"><span class="partner-name">Nimbus Cloud</span><span class="partner-note">partner network</span></div>
    <div class="partner"><span class="partner-name">Corvid Software</span><span class="partner-note">Solutions Partner</span></div>
    <div class="partner"><span class="partner-name">Keystone Infra</span><span class="partner-note">Partner Network</span></div>
  </div>

  <div class="abs quality">
    <div class="quality-flag"><svg viewBox="0 0 28 32" fill="none" stroke="#fff" stroke-width="1.8"><path d="M14 2l11 4v9c0 7-5 12-11 15C8 27 3 22 3 15V6z"/><path d="M9 16l4 4 7-8"/></svg></div>
    <h4>COMMITTED TO QUALITY &amp; SECURITY</h4>
    <p>We follow industry-leading frameworks and best practices to ensure secure, reliable and compliant delivery.</p>
    <div class="quality-divider"></div>
    <div class="cert" style="top:12px">
      <div class="cert-seal"></div>
      <div class="cert-text"><small>ISO</small><b>27001</b><span>Information Security<br>Management</span></div>
    </div>
    <div class="cert" style="top:74px">
      <div class="cert-seal"></div>
      <div class="cert-text"><small>ISO</small><b>9001</b><span>Quality Management</span></div>
    </div>
  </div>

  <!-- footer -->
  <div class="abs cta-band">
    <div class="cta">
      <h5>LET’S BUILD WHAT’S NEXT.</h5>
      <p>Partner with Brightwell Systems to accelerate your cloud journey and achieve lasting impact.</p>
    </div>
    <div class="contact" style="left:324px">
      <div class="contact-dot"><svg viewBox="0 0 19 19" fill="none" stroke="#fff" stroke-width="1.5"><rect x="2" y="4" width="15" height="11" rx="1"/><path d="M2 5l7.5 6L17 5"/></svg></div>
      <div><b>EMAIL</b><span>info@brightwell.example</span></div>
    </div>
    <div class="contact" style="left:505px">
      <div class="contact-dot"><svg viewBox="0 0 19 19" fill="none" stroke="#fff" stroke-width="1.4"><circle cx="9.5" cy="9.5" r="7.5"/><ellipse cx="9.5" cy="9.5" rx="3.5" ry="7.5"/><path d="M2 9.5h15M3 5.5h13M3 13.5h13"/></svg></div>
      <div><b>WEBSITE</b><span>www.brightwell.example</span></div>
    </div>
    <div class="contact" style="left:682px">
      <div class="contact-dot"><svg viewBox="0 0 19 19" fill="#fff"><path d="M5 2l3 3-1.6 2.2a9 9 0 0 0 5.4 5.4L14 11l3 3-2 2.5C9 16 3 10 2.5 4z"/></svg></div>
      <div><b>PHONE</b><span>+61 2 5550 0147</span></div>
    </div>
  </div>

  <div class="abs signoff"><b>BRIGHTWELL SYSTEMS</b><i></i><span>INNOVATE. OPTIMISE. TRANSFORM.</span></div>
</div>
</body>
</html>
```